Stationary and business card design for dental office
Dental Harbor
Simple
Merrow T. Pashley, DMD
Dental Harbor (use logo)
2870 W. Cobalt Mesa Rd. Ste #6
Las Vegas, NV 89047
pashleydmd@quarvix-mail.test
www.ourdentalharbor.test
Front of card to be gloss finish with the back to be a regular paper finish so that appointments can be written on the back.
My Next Appointment
Date:___________
Time:____________
Days of the week with boxes
Call Now
A simple map of the location to the right

```html
<!DOCTYPE html>
<html lang="en">
<head>
<meta charset="utf-8">
<title>Dental Harbor — Stationery Set</title>
<link rel="stylesheet" href="https://fonts.googleapis.com/css2?family=Open+Sans:wght@400;600;700&display=swap">
<style>
  :root {
    --page-bg: #ffffff;
    --sheet: #ffffff;
    --sheet-edge: #d9dde3;
    --navy: #1d3f86;
    --blue: #2a62b8;
    --sky: #6aa6e0;
    --gold: #c9a640;
    --green: #7fae3a;
    --ink: #4a4f57;
    --muted: #8a9099;
    --faint: #eef1f5;
    --map: #2b2f36;
  }
  * { box-sizing: border-box; margin: 0; padding: 0; }
  html, body { width: 1200px; height: 871px; overflow: hidden; background: var(--page-bg); }
  body { position: relative; font-family: "Open Sans", Arial, sans-serif; color: var(--ink); }

  .sheet {
    position: absolute; background: var(--sheet);
    box-shadow: 0 0 0 1px var(--sheet-edge), 0 2px 5px rgba(0,0,0,.12);
    overflow: hidden;
  }
  .letterhead { left: 187px; top: 67px; width: 408px; height: 528px; }
  .fax-sheet  { left: 605px; top: 67px; width: 413px; height: 528px; }
  .envelope   { left: 187px; top: 610px; width: 413px; height: 190px; }
  .card-front { left: 670px; top: 612px; width: 168px; height: 98px; }
  .card-back  { left: 845px; top: 612px; width: 173px; height: 98px; }

  .header-wave { position: absolute; left: 0; top: 0; width: 100%; height: 80px; display: block; }
  .envelope .header-wave { height: 60px; }

  .brand {
    position: absolute; left: 24px; top: 30px;
    display: flex; align-items: center; gap: 6px;
    font-weight: 700; font-size: 17px; color: var(--navy); line-height: 1;
  }
  .brand-dot { width: 18px; height: 18px; border-radius: 50%; background: var(--sky); }
  .envelope .brand { left: 20px; top: 24px; font-size: 15px; }

  .faint-mark {
    position: absolute; left: 50%; top: 46%; width: 150px; height: 150px;
    margin-left: -75px; margin-top: -75px; border-radius: 50%; background: var(--faint);
  }

  .footer {
    position: absolute; left: 0; right: 0; bottom: 26px;
    text-align: center; font-size: 5.5px; color: var(--muted); line-height: 1.7;
  }
  .footer span { margin: 0 10px; }

  .fax-fields {
    position: absolute; left: 26px; top: 96px; width: 360px;
    display: grid; grid-template-columns: 1fr 1fr; column-gap: 22px; row-gap: 5px;
    font-size: 6.5px; color: var(--ink);
  }
  .fax-field { display: flex; align-items: flex-end; gap: 4px; }
  .fax-field b { font-weight: 600; width: 28px; }
  .fax-field i { flex: 1; border-bottom: 0.7px solid var(--muted); height: 7px; }
  .fax-checks {
    position: absolute; left: 26px; top: 152px; display: flex; gap: 10px;
    font-size: 5.5px; color: var(--ink);
  }
  .fax-checks label { display: flex; align-items: center; gap: 3px; }
  .fax-checks label::before { content: ""; width: 6px; height: 6px; border: 0.7px solid var(--muted); }

  .envelope .return-address {
    position: absolute; left: 22px; top: 58px; font-size: 5px; color: var(--muted); line-height: 1.6;
  }
  .envelope .faint-mark { left: 30px; top: auto; bottom: -40px; margin: 0; width: 90px; height: 90px; }

  /* business card front */
  .card-front .card-band {
    position: absolute; left: 0; top: 0; width: 100%; height: 22px;
    background: linear-gradient(90deg, var(--navy), var(--blue) 60%, var(--sky));
    color: #fff; font-size: 4.6px; padding: 5px 8px; line-height: 1.4;
  }
  .card-front .card-band::after {
    content: ""; position: absolute; left: 0; right: 0; bottom: -2px; height: 2px;
    background: linear-gradient(90deg, var(--gold), var(--green));
  }
  .card-front .brand { left: 56px; top: 38px; font-size: 10px; gap: 4px; }
  .card-front .brand-dot { width: 10px; height: 10px; }
  .card-front .card-contact {
    position: absolute; left: 8px; bottom: 7px; font-size: 4.2px; line-height: 1.5; color: var(--ink);
  }
  .card-front .card-contact strong { color: var(--navy); font-size: 5px; }

  /* business card back */
  .card-back .appointment {
    position: absolute; left: 8px; top: 8px; width: 86px; font-size: 5px; color: var(--ink);
  }
  .card-back .appointment h2 { font-size: 5.6px; font-weight: 700; color: var(--navy); margin-bottom: 5px; }
  .card-back .slot { display: flex; gap: 3px; margin-bottom: 5px; align-items: flex-end; }
  .card-back .slot i { flex: 1; border-bottom: 0.6px solid var(--muted); height: 5px; }
  .card-back .days { display: flex; gap: 2px; font-size: 3.8px; }
  .card-back .days span { display: flex; flex-direction: column; align-items: center; gap: 1px; }
  .card-back .days span::after { content: ""; width: 7px; height: 7px; border: 0.6px solid var(--navy); }
  .card-back .call-now {
    position: absolute; left: 8px; bottom: 7px; font-size: 5px; font-weight: 700; color: var(--blue);
  }
  .card-back .location-map {
    position: absolute; right: 7px; top: 20px; width: 70px; height: 44px;
    background: linear-gradient(135deg, #3a3f47, var(--map)); border-radius: 2px;
  }
  .card-back .card-strip {
    position: absolute; left: 0; right: 0; bottom: 0; height: 4px;
    background: linear-gradient(90deg, var(--navy), var(--sky));
  }
</style>
</head>
<body>

<svg width="0" height="0" style="position:absolute">
  <defs>
    <linearGradient id="wave-blue" x1="0" y1="0" x2="1" y2="1">
      <stop offset="0" stop-color="#6aa6e0"/>
      <stop offset=".5" stop-color="#2a62b8"/>
      <stop offset="1" stop-color="#1d3f86"/>
    </linearGradient>
    <symbol id="wave" viewBox="0 0 400 80" preserveAspectRatio="none">
      <path d="M0 0H400V58C300 76 200 30 90 22 50 19 20 18 0 20Z" fill="url(#wave-blue)"/>
      <path d="M0 24C30 22 70 24 110 30 210 44 300 80 400 64" fill="none" stroke="#c9a640" stroke-width="2.2"/>
      <path d="M0 28C40 26 90 30 130 37 220 52 310 86 400 70" fill="none" stroke="#7fae3a" stroke-width="2.2"/>
    </symbol>
  </defs>
</svg>

<section class="sheet letterhead" aria-label="Letterhead">
  <svg class="header-wave" aria-hidden="true"><use href="#wave"/></svg>
  <div class="brand"><span class="brand-dot"></span>Dental Harbor</div>
  <div class="faint-mark" aria-hidden="true"></div>
  <div class="footer">
    <div>2870 W. Cobalt Mesa Rd. Ste #6 · Las Vegas, NV 89047</div>
    <div><span>Phone: 702.555.0148</span><span>Fax: 702.555.0149</span><span>www.ourdentalharbor.test</span></div>
  </div>
</section>

<section class="sheet fax-sheet" aria-label="Fax cover sheet">
  <svg class="header-wave" aria-hidden="true"><use href="#wave"/></svg>
  <div class="brand"><span class="brand-dot"></span>Dental Harbor</div>
  <div class="fax-fields">
    <div class="fax-field"><b>To:</b><i></i></div>
    <div class="fax-field"><b>From:</b><i></i></div>
    <div class="fax-field"><b>Fax:</b><i></i></div>
    <div class="fax-field"><b>Pages:</b><i></i></div>
    <div class="fax-field"><b>Phone:</b><i></i></div>
    <div class="fax-field"><b>Date:</b><i></i></div>
    <div class="fax-field"><b>Re:</b><i></i></div>
    <div class="fax-field"><b>CC:</b><i></i></div>
  </div>
  <div class="fax-checks">
    <label>Urgent</label><label>For Review</label><label>Please Comment</label><label>Please Reply</label><label>Please Recycle</label>
  </div>
  <div class="faint-mark" aria-hidden="true"></div>
  <div class="footer">
    <div>2870 W. Cobalt Mesa Rd. Ste #6 · Las Vegas, NV 89047</div>
    <div><span>Phone: 702.555.0148</span><span>Fax: 702.555.0149</span><span>www.ourdentalharbor.test</span></div>
  </div>
</section>

<section class="sheet envelope" aria-label="Envelope">
  <svg class="header-wave" aria-hidden="true"><use href="#wave"/></svg>
  <div class="brand"><span class="brand-dot"></span>Dental Harbor</div>
  <div class="return-address">2870 W. Cobalt Mesa Rd. Ste #6<br>Las Vegas, NV 89047</div>
  <div class="faint-mark" aria-hidden="true"></div>
</section>

<section class="sheet card-front" aria-label="Business card front">
  <div class="card-band">www.ourdentalharbor.test<br>Family &amp; Cosmetic Dentistry</div>
  <div class="brand"><span class="brand-dot"></span>Dental Harbor</div>
  <div class="card-contact">
    <strong>Merrow T. Pashley, DMD</strong><br>
    2870 W. Cobalt Mesa Rd. Ste #6<br>
    Las Vegas, NV 89047<br>
    pashleydmd@quarvix-mail.test
  </div>
</section>

<section class="sheet card-back" aria-label="Business card back">
  <div class="appointment">
    <h2>My Next Appointment</h2>
    <div class="slot">Date:<i></i></div>
    <div class="slot">Time:<i></i></div>
    <div class="days"><span>M</span><span>T</span><span>W</span><span>T</span><span>F</span><span>S</span></div>
  </div>
  <div class="call-now">Call Now 702.555.0148</div>
  <div class="location-map" role="img" aria-label="Simple map showing the office location"></div>
  <div class="card-strip" aria-hidden="true"></div>
</section>

</body>
</html>
```